Logo and website for new private wealth management business

This project is for a new company website and logo. The name of the firm is Harborline Estate Partners, LLC. We are a wealth management firm offering customized financial planning and investment management services to high net worth and ultra high net worth individuals and families. I want the website to feel contemporary but convey a feeling of sophistication and prestige.
www.tallowridgeholdings.example and www.qnfunds.example are both good reference websites.
My clients will consist of wealthy individuals and families. I have existing clients in their 50s - 70s, but I also intend to target younger business owners and entrepreneurs in their 30s -50s.

Target Market(s)

Business owners, entrepreneurs and corporate executives. Many existing clients are in their 60s and 70s, but intend to also attract a younger clientele in their 30s - 50s.

Industry/Entity Type

Wealth management, investment advisory, financial planning

Coding

Coded - Design and coding required

Colors
0054AA
0677BA
7BADD7
CADEEF
E8F1F8
0094D4
00A9DD
6FCCEA
C7EBF8
E9F6FB
00AB8E
00BBA5
67D7C9
C6EFE9
E9F9F6
EE7325
F08F49
F5BC92
FAE3D3
FDF4ED

Requirements
Must have
• Should use blue as the main color theme. Should have an About, Services, Our Clients, FAQ, and Contact sections
Should not have
• Should not have pictures of people as the background.

```html
<!DOCTYPE html>
<html lang="en">
<head>
<meta charset="utf-8">
<title>Harborline Estate Partners, LLC</title>
<link href="https://fonts.googleapis.com/css2?family=Montserrat:wght@500;600;700;800&family=Roboto:wght@400;500&display=swap" rel="stylesheet">
<style>
:root{
  --blue:#0a3f9c;
  --blue-mid:#0054aa;
  --sky:#0677ba;
  --teal:#00ab8e;
  --green:#3fb08f;
  --orange:#e85d1f;
  --peach:#fae3d3;
  --ink:#1f1f1f;
  --grey:#555;
  --black:#000;
  --white:#fff;
  --head:'Montserrat',sans-serif;
  --body:'Roboto',sans-serif;
}
*{margin:0;padding:0;box-sizing:border-box}
html,body{width:1200px;height:3466px;overflow:hidden;background:var(--white)}
body{position:relative;font-family:var(--body);color:var(--ink)}
.abs{position:absolute}
.btn{position:absolute;background:var(--orange);color:var(--white);font-family:var(--head);font-weight:700;font-size:16px;display:flex;align-items:center;justify-content:center;text-transform:uppercase}

/* header */
.site-header{position:absolute;left:0;top:0;width:1200px;height:117px;background:var(--white)}
.brand{position:absolute;display:flex;align-items:center;gap:14px}
.brand-mark{width:44px;height:44px;background:var(--blue)}
.brand-name{font-family:var(--head);font-weight:600;color:var(--blue);line-height:1.15}
.brand-name small{display:block;font-size:14px;font-weight:500}
.header-brand{left:110px;top:30px}
.header-brand .brand-name{font-size:28px}
.main-nav{position:absolute;left:459px;top:47px;display:flex;gap:46px;font-size:15px;color:#333}
.login{left:968px;top:34px;width:118px;height:46px}

/* hero */
.hero{position:absolute;left:0;top:117px;width:1200px;height:730px;background:linear-gradient(100deg,#dfe4ea 0%,#b9c3cf 45%,#5f6d80 70%,#2f3a4a 100%)}
.hero-title{position:absolute;left:110px;top:240px;font-family:var(--head);font-weight:800;font-size:66px;line-height:85px;color:var(--blue)}
.hero-title .accent{color:var(--green)}
.get-started{left:110px;top:520px;width:143px;height:46px}
.dots{position:absolute;left:570px;top:696px;display:flex;gap:8px;align-items:center}
.dots span{width:11px;height:11px;border-radius:50%;background:var(--white)}
.dots .on{width:20px;height:20px;background:var(--orange);border:3px solid var(--white)}
.hero-edge{position:absolute;left:0;top:720px}

/* about */
.about{position:absolute;left:0;top:847px;width:1200px;height:408px;background:linear-gradient(90deg,#eef0f3 0%,#f6f7f8 50%,#e9ecf0 100%)}
.section-title{position:absolute;font-family:var(--head);font-weight:700;font-size:30px;color:var(--blue);text-transform:uppercase}
.section-title span{color:var(--sky)}
.about-title{left:0;width:1200px;text-align:center;top:895px}
.about-text{position:absolute;left:228px;width:744px;top:966px;text-align:center;font-size:15px;line-height:26px;color:#222}
.about-btn{left:523px;top:1137px;width:154px;height:55px}

/* services */
.services-title{left:0;width:1200px;text-align:center;top:1336px}
.peach-circle{position:absolute;left:904px;top:1328px;width:250px;height:250px;border-radius:50%;background:var(--peach);opacity:.7}
.service-heading{position:absolute;font-family:var(--head);font-weight:500;font-size:26px}
.service-text{position:absolute;font-size:15px;line-height:26px}
.plan-heading{left:111px;top:1433px;color:var(--ink)}
.plan-text{left:111px;top:1490px;width:450px;color:var(--grey)}
.plan-btn{left:111px;top:1707px;width:153px;height:56px}
.dot-grid{position:absolute;left:620px;top:1560px}
.plan-photo{position:absolute;left:667px;top:1422px;width:377px;height:343px;background:linear-gradient(135deg,#3c5a78 0%,#8ea3b8 50%,#d7dde3 100%)}

.invest{position:absolute;left:0;top:1890px;width:1200px;height:487px;background:linear-gradient(90deg,#cfd6dd 0%,#9aa8b8 30%,#5d6f8a 45%,#0a3f9c 62%,#0a3f9c 100%)}
.invest-heading{left:629px;top:1964px;color:var(--white)}
.invest-text{left:629px;top:2021px;width:450px;color:#e8eefa}
.invest-btn{left:629px;top:2239px;width:153px;height:56px}

/* news */
.news-title{left:111px;top:2456px;text-align:left}
.card{position:absolute;top:2525px;width:315px}
.card-photo{width:315px;height:195px;background:linear-gradient(135deg,#6f7a86,#c9ccd0)}
.card-date{position:absolute;left:27px;top:173px;width:143px;height:42px;background:var(--teal);color:var(--white);font-family:var(--head);font-weight:600;font-size:12px;display:flex;align-items:center;justify-content:center}
.card h3{margin-top:38px;font-family:var(--head);font-weight:500;font-size:19.5px;line-height:28px}
.card p{margin-top:12px;font-size:15px;line-height:26px;color:var(--grey)}
.card .read{display:block;margin-top:12px;font-family:var(--head);font-weight:700;font-size:15px;color:var(--orange)}

/* footer */
.footer{position:absolute;left:0;top:2979px;width:1200px;height:487px;background:var(--black);color:var(--white)}
.footer-edge{position:absolute;left:0;top:2975px}
.footer-brand{left:110px;top:3218px}
.footer-brand .brand-name{color:var(--white);font-size:31px}
.footer-brand .brand-name small{font-size:15px}
.social{position:absolute;left:110px;top:3320px;display:flex;gap:15px}
.social span{width:40px;height:40px;border-radius:50%;background:var(--white)}
.foot-head{position:absolute;top:3178px;font-family:var(--head);font-weight:600;font-size:19px;color:var(--white)}
.quick{position:absolute;left:420px;top:3224px;list-style:none;font-size:15px;line-height:27px}
.contact-item{position:absolute;left:586px;display:flex;gap:12px;font-size:15px;line-height:23px}
.contact-item svg{flex:none;margin-top:3px}
.news-form{position:absolute;left:861px;top:3229px;width:225px;height:39px;background:var(--white);border-radius:4px;display:flex}
.news-form .field{flex:1;color:#888;font-size:15px;padding:10px 14px}
.news-form .send{width:53px;background:var(--orange);border-radius:4px;display:flex;align-items:center;justify-content:center}
.copyright{position:absolute;left:0;width:1200px;top:3414px;text-align:center;font-size:15px}
</style>
</head>
<body>

<header class="site-header">
  <div class="brand header-brand">
    <div class="brand-mark"></div>
    <div class="brand-name">HARBORLINE<small>ESTATE PARTNERS, LLC</small></div>
  </div>
  <nav class="main-nav"><span>HOME</span><span>ABOUT</span><span>SERVICES</span><span>BLOG</span><span>CONTACT</span></nav>
  <div class="btn login">Log In</div>
</header>

<section class="hero" role="img" aria-label="Hourglass, glass globe and stacks of coins on a reflective table"></section>
<h1 class="hero-title">HARBORLINE<br><span class="accent">ESTATE</span><br>PARTNERS</h1>
<div class="btn get-started">Get Started</div>
<div class="dots"><span></span><span class="on"></span><span></span></div>
<svg class="hero-edge" width="1200" height="130" viewBox="0 0 1200 130">
  <defs>
    <linearGradient id="heroBand" x1="0" y1="0" x2="1" y2="0">
      <stop offset="0" stop-color="#1d3f9a"/>
      <stop offset="0.5" stop-color="#c4551f"/>
      <stop offset="0.7" stop-color="#e85d1f"/>
      <stop offset="1" stop-color="#d4612b"/>
    </linearGradient>
  </defs>
  <polygon points="0,125 847,7 1200,70 1200,130 0,130" fill="url(#heroBand)"/>
  <polygon points="0,130 847,40 1200,94 1200,130" fill="#eef0f3"/>
</svg>

<section class="about" role="img" aria-label="Advisor reviewing financial documents with a pen, softly faded"></section>
<h2 class="section-title about-title">About <span>Us</span></h2>
<p class="about-text">Lorem ipsum dolor sit amet, consectetur adipiscing elit, sed do eiusmod tempor incididunt ut labore et dolore magna aliqua.Ut enim ad minim veniam, quis nostrud exercitation ullamco laboris nisi ut aliquip ex ea commodo consequat. Duis aute irure dolor in reprehenderit in voluptate velit esse cillum dolore eu fugiat nulla pariatur. Excepteur sint occaecat cupidatat non proident, sunt in culpa qui officia deserunt mollit anim id est laborum.</p>
<div class="btn about-btn">Learn More</div>

<h2 class="section-title services-title">Our <span>Services</span></h2>
<div class="peach-circle"></div>
<h3 class="service-heading plan-heading">Financial Planning</h3>
<p class="service-text plan-text">Lorem ipsum dolor sit amet, consectetur adipiscing elit, sed do eiusmod tempor incididunt ut labore et dolore magna aliqua.Ut enim ad minim veniam, quis nostrud exercitation ullamco laboris nisi ut aliquip ex ea commodo consequat. Duis aute irure dolor in reprehenderit in voluptate velit esse cillum dolore eu fugiat nulla pariatur. Excepteur sint occaecat cupidatat non proident, sunt in culpa qui officia deserunt mollit anim id est laborum.</p>
<div class="btn plan-btn">Learn More</div>
<svg class="dot-grid" width="250" height="245">
  <defs><pattern id="dotp" width="12" height="12" patternUnits="userSpaceOnUse"><circle cx="3" cy="3" r="1.4" fill="#00ab8e"/></pattern></defs>
  <rect x="0" y="0" width="48" height="245" fill="url(#dotp)"/>
  <rect x="0" y="200" width="250" height="45" fill="url(#dotp)"/>
</svg>
<div class="plan-photo" role="img" aria-label="Senior couple meeting with an advisor holding a tablet"></div>

<section class="invest" role="img" aria-label="Businessman working at a laptop, blending into a blue panel"></section>
<h3 class="service-heading invest-heading">Investment Management</h3>
<p class="service-text invest-text">Lorem ipsum dolor sit amet, consectetur adipiscing elit, sed do eiusmod tempor incididunt ut labore et dolore magna aliqua.Ut enim ad minim veniam, quis nostrud exercitation ullamco laboris nisi ut aliquip ex ea commodo consequat. Duis aute irure dolor in reprehenderit in voluptate velit esse cillum dolore eu fugiat nulla pariatur. Excepteur sint occaecat cupidatat non proident, sunt in culpa qui officia deserunt mollit anim id est laborum.</p>
<div class="btn invest-btn">Learn More</div>

<h2 class="section-title news-title">Latest <span>News</span></h2>
<article class="card" style="left:111px">
  <div class="card-photo" role="img" aria-label="Couple reviewing papers with an advisor"></div>
  <div class="card-date">21 December,2022</div>
  <h3>Sed ut perspiciatis unde omnis iste natus error sit volupt</h3>
  <p>Lorem ipsum dolor sit amet, consectetur adipiscing elit, sed do eiusmod tempor</p>
  <span class="read">READ MORE</span>
</article>
<article class="card" style="left:442px">
  <div class="card-photo" role="img" aria-label="Business team discussing documents at a desk"></div>
  <div class="card-date">21 December,2022</div>
  <h3>Sed ut perspiciatis unde omnis iste natus error sit volupt</h3>
  <p>Lorem ipsum dolor sit amet, consectetur adipiscing elit, sed do eiusmod tempor</p>
  <span class="read">READ MORE</span>
</article>
<article class="card" style="left:773px">
  <div class="card-photo" role="img" aria-label="Colleagues meeting around a laptop in an office lounge"></div>
  <div class="card-date">21 December,2022</div>
  <h3>Sed ut perspiciatis unde omnis iste natus error sit volupt</h3>
  <p>Lorem ipsum dolor sit amet, consectetur adipiscing elit, sed do eiusmod tempor</p>
  <span class="read">READ MORE</span>
</article>

<footer class="footer"></footer>
<svg class="footer-edge" width="1200" height="135" viewBox="0 0 1200 135">
  <defs>
    <linearGradient id="footBand" x1="0" y1="0" x2="0.7" y2="1">
      <stop offset="0" stop-color="#e85d1f"/>
      <stop offset="0.55" stop-color="#7a4a6a"/>
      <stop offset="1" stop-color="#2d54b8"/>
    </linearGradient>
  </defs>
  <polygon points="0,0 1200,0 1200,30 847,128 0,4" fill="url(#footBand)"/>
  <polygon points="0,0 1200,0 1200,22 847,100 0,10" fill="#fff"/>
</svg>
<div class="brand footer-brand">
  <div class="brand-mark" style="background:var(--white)"></div>
  <div class="brand-name">HARBORLINE<small>ESTATE PARTNERS, LLC</small></div>
</div>
<div class="social"><span></span><span></span><span></span><span></span></div>

<div class="foot-head" style="left:420px">QUICK LINKS</div>
<ul class="quick"><li>Home</li><li>About</li><li>Services</li><li>Blog</li><li>Contact</li></ul>

<div class="foot-head" style="left:586px">CONTACT US</div>
<div class="contact-item" style="top:3236px">
  <svg width="16" height="20" viewBox="0 0 16 20"><path d="M8 0a7 7 0 0 0-7 7c0 5 7 13 7 13s7-8 7-13a7 7 0 0 0-7-7zm0 10a3 3 0 1 1 0-6 3 3 0 0 1 0 6z" fill="#fff"/></svg>
  <span>Lorem ipsum dolor sit amet,<br>consectetur</span>
</div>
<div class="contact-item" style="top:3300px">
  <svg width="18" height="18" viewBox="0 0 24 24"><path d="M6.6 10.8a15 15 0 0 0 6.6 6.6l2.2-2.2a1 1 0 0 1 1-.25 11.4 11.4 0 0 0 3.6.57 1 1 0 0 1 1 1V20a1 1 0 0 1-1 1A17 17 0 0 1 3 4a1 1 0 0 1 1-1h3.5a1 1 0 0 1 1 1c0 1.25.2 2.45.57 3.57a1 1 0 0 1-.25 1z" fill="#fff"/></svg>
  <span>+1 (555) 010 4410</span>
</div>
<div class="contact-item" style="top:3334px">
  <svg width="18" height="14" viewBox="0 0 18 14"><path d="M0 0h18v14H0z" fill="#fff"/><path d="M0 0l9 7 9-7" fill="none" stroke="#000" stroke-width="1.5"/></svg>
  <span>info@harborlineestate.example</span>
</div>

<div class="foot-head" style="left:861px">NEWSLETTER</div>
<div class="news-form">
  <span class="field">Enter email</span>
  <span class="send"><svg width="16" height="12" viewBox="0 0 16 12"><path d="M0 0h16v12H0z" fill="#fff"/><path d="M0 0l8 6 8-6" fill="none" stroke="#e85d1f" stroke-width="1.5"/></svg></span>
</div>

<p class="copyright">©Copyrights 2022 Harborline Estate Partners &nbsp;&nbsp;|&nbsp;&nbsp; All Rights Reserved</p>

</body>
</html>
```